we are an outdoor outlet in a country club that has a variety of outlets. The Club is called Brookhaven and is located in Cairo, Egypt. This garden menu will include cuisines from the Mediterranean, Asia and Texmex. we need a menu that is colorful and would fit an A3 size, back and front are to be used. Attached is the old menu currently in use (Garden Menu 2012.pdf is just for reference) and the new menu text for you to use is under the name Garden Menu Fall 2013
thank you.

```html
<!DOCTYPE html>
<html lang="en">
<head>
<meta charset="utf-8">
<title>Garden Menu – Mediterranean Corner</title>
<link href="https://fonts.googleapis.com/css2?family=Arimo:wght@400;700&family=Exo+2:wght@800&display=swap" rel="stylesheet">
<style>
  :root {
    --cream: #fde49a;
    --brown: #5a2a0b;
    --forest: #0e4a1d;
    --lime: #b6c832;
    --ink: #2b1a0c;
    --white: #ffffff;
    --logo-ink: #6f7d1c;
  }
  * { margin: 0; padding: 0; box-sizing: border-box; }
  html, body { width: 1200px; height: 849px; overflow: hidden; background: var(--white); }
  .menu { position: relative; width: 1200px; height: 849px; background: var(--cream); font-family: "Arimo", Arial, sans-serif; color: var(--ink); }
  .header { position: absolute; left: 0; top: 0; width: 1200px; height: 140px; background: var(--white); }
  .brand { position: absolute; top: 56px; display: flex; align-items: center; gap: 10px; font-family: "Arimo", Arial, sans-serif; font-size: 27px; font-weight: 400; color: var(--logo-ink); }
  .brand__dot { width: 26px; height: 26px; border-radius: 50%; background: var(--lime); }
  .brand--left { left: 78px; }
  .brand--right { left: 955px; }
  .title { position: absolute; left: 0; width: 1200px; top: 16px; text-align: center; font-family: "Exo 2", sans-serif; font-weight: 800; font-size: 60px; letter-spacing: 1px; color: var(--forest); line-height: 1; }
  .corner { position: absolute; left: 385px; top: 91px; width: 430px; height: 40px; border-radius: 8px; background: var(--forest); color: var(--lime); font-weight: 700; font-size: 27px; text-align: center; line-height: 40px; }
  .band { position: absolute; left: 0; top: 140px; width: 1200px; height: 47px; background: var(--brown); }
  .band__heading { position: absolute; top: 12px; color: var(--white); font-weight: 700; font-size: 25px; line-height: 1; }
  .price-col { position: absolute; background: var(--white); }
  .item-bar { position: absolute; height: 17px; background: var(--brown); color: var(--white); font-weight: 700; font-size: 12.5px; line-height: 17px; }
  .item-bar__price { position: absolute; left: 247px; font-size: 14px; }
  .item-desc { position: absolute; font-size: 12.5px; line-height: 16px; }
  .appetizers { position: absolute; left: 355px; top: 199px; width: 316px; list-style: none; font-size: 12.5px; line-height: 16px; text-align: justify; }
  .photo { position: absolute; }
</style>
</head>
<body>
<main class="menu">
  <header class="header">
    <div class="brand brand--left"><span class="brand__dot"></span>Brookhaven</div>
    <h1 class="title">GARDEN MENU</h1>
    <div class="corner">Mediterranean Corner</div>
    <div class="brand brand--right"><span class="brand__dot"></span>Brookhaven</div>
  </header>

  <div class="band">
    <h2 class="band__heading" style="left:73px">Soups</h2>
    <h2 class="band__heading" style="left:428px">Appetizers:</h2>
    <h2 class="band__heading" style="left:874px">Salads:</h2>
  </div>

  <!-- Soups -->
  <div class="price-col" style="left:252px; top:188px; width:82px; height:163px"></div>
  <div class="item-bar" style="left:15px; top:198px; width:319px; padding-left:7px">Tomato Basil</div>
  <p class="item-desc" style="left:22px; top:215px; width:220px">Simmered tomato soup finished with fresh basil and cream</p>
  <div class="item-bar" style="left:15px; top:246px; width:319px; padding-left:7px">Chicken Cream</div>
  <p class="item-desc" style="left:22px; top:263px; width:225px">Chicken broth with roasted chicken cubes, pine nuts, and cream</p>
  <div class="item-bar" style="left:15px; top:295px; width:319px; padding-left:7px">Moroccan Harira<span class="item-bar__price">LE 28.00</span></div>
  <p class="item-desc" style="left:22px; top:312px; width:225px">Vegetable broth with fresh tomato, chickpeas, lentil, cilantro, and diced lamb</p>
  <div class="photo" role="img" aria-label="Tomato basil soup in a green bowl" style="left:20px; top:379px; width:209px; height:234px; background:linear-gradient(135deg,#e6e2d6,#e07a45 55%,#a6c23a)"></div>
  <div class="photo" role="img" aria-label="Harira soup in a red pot topped with herbs" style="left:54px; top:630px; width:145px; height:151px; background:radial-gradient(circle at 50% 45%,#9a5a2a,#c0392b 60%,#e8e2d8)"></div>

  <!-- Appetizers -->
  <ul class="appetizers">
    <li>Salmontartare seasoned with lemon juice, garlic, and crushed black pepper</li>
    <li>Roasted eggplant rolls with herbed ricotta cheese and pine nuts</li>
    <li>Falafel in mini pita served with tehina and oriental salsa</li>
    <li>Mankousha with thyme and olive oil</li>
    <li>Fried kobeba with minced meat, spices, and pine nuts</li>
    <li>Fried calamari a la Romana served with aioli</li>
    <li>Samboussek with herbed white cheese and mint</li>
    <li>Oriental sausage sautéed with garlic and onion</li>
    <li>Mini vine leaves with a yoghurt dip</li>
    <li>Fatouch with a pomegranate syrup dressing</li>
    <li>Hummus seasoned with lemon juice, garlic, and olive oil</li>
    <li>White cheese with diced tomato, thyme, and olive oil</li>
    <li>Tehina seasoned with cumin, lemon juice, and garlic</li>
  </ul>
  <div class="price-col" style="left:697px; top:196px; width:83px; height:636px"></div>
  <div class="photo" role="img" aria-label="Chopped onion, tomato and parsley in a bowl" style="left:357px; top:454px; width:291px; height:183px; background:linear-gradient(100deg,#d9c7c9 30%,#d9532b 55%,#3f6b22 80%)"></div>
  <div class="photo" role="img" aria-label="Hummus with pita bread and cucumber slices" style="left:357px; top:646px; width:291px; height:194px; background:linear-gradient(160deg,#8a5a38,#e8dcc0 45%,#b98a52 75%,#4a2d1a)"></div>

  <!-- Salads -->
  <div class="price-col" style="left:1097px; top:193px; width:83px; height:246px"></div>
  <div class="item-bar" style="left:798px; top:199px; width:381px; padding-left:18px">Caprese</div>
  <p class="item-desc" style="left:816px; top:215px; width:170px">Buffalo mozzarella and sliced tomato with a balsamic vinaigrette</p>
  <div class="item-bar" style="left:798px; top:263px; width:381px; padding-left:18px">Rocket Apple</div>
  <p class="item-desc" style="left:816px; top:279px; width:261px; text-align:justify">Rocket leaves with gorgonzola, croutons, and strawberry<br>vinaigrette</p>
  <div class="item-bar" style="left:798px; top:327px; width:381px; padding-left:18px">French Riviera Nicoise</div>
  <p class="item-desc" style="left:816px; top:343px; width:261px; text-align:justify">Lettuce, egg, tomato, tuna,<br>olives, onion, celery, radish, bell pepper in a French vinaigrette</p>
  <div class="item-bar" style="left:798px; top:392px; width:381px; padding-left:18px">Folle</div>
  <p class="item-desc" style="left:816px; top:408px; width:265px">Mixed greens with crab sticks, mushroom, corn, cherry tomato in a mango vinaigrette</p>
  <div class="photo" role="img" aria-label="Fresh salad vegetables on a wooden board" style="left:805px; top:456px; width:324px; height:244px; background:linear-gradient(120deg,#7fb23a,#f4f2ee 35%,#d9402a 55%,#3e7a2a 80%,#c9a070)"></div>
  <div class="photo" role="img" aria-label="Strawberry and rocket salad on a plate" style="left:883px; top:706px; width:170px; height:126px; background:radial-gradient(circle,#d63a2a,#4f8f2f 55%,#f3f3f0)"></div>
</main>
</body>
</html>
```